Our Chalet for rent needs a new website

Hi guys we have a chalet for rent and we finally want to have our own website for information and bookings the information is posted below and will upload pictures in due course.

Thanks

Chalet | 5 bedrooms | sleeps 11

Key Info
Beach or lakeside relaxationSkiGreat for children of all agesSome pets are welcome - please contact the ownerPrivate gardenCar advised
Exceptionally renovated Fern Byre dates from 1781 and offers the discerning skier a chance to stay in a wonderful mountain lodge. Spacious and light, there is a superb double aspect living and dining area and open-plan kitchen. All bedrooms are ensuite,and facilities include a sauna, enormous 6m 'Swim spa' hot tub, open-fireplace and separate treatment room on request. This chalet is perfect for families and groups!

Previously featured in Plate and Journey magazine and The Courier, chalet Fern Byre can be counted as one of only a handful of authentic farmhouses in the Chamonix valley available for rental. Located in the charming village of Les Houches, only minutes walk to the ski and mountain bike lifts, amenities, shops and several delightful restaurants and just a short drive from Chamonix town and the other ski/bike areas of the Chamonix valley.

The chalet is run as a luxury boutique hotel and is offered with total flexibility in mind. In winter the chalet provides luxury catered or self catered accommodation. In summer the chalet can be offered B&B or self catered. Our service can include in resort driving, airport transfers, and as experienced professionals with more than 27 yrs experience in Chamonix your holiday will be expertly delivered, whatever formula you choose!

Size Sleeps up to 11, 5 bedrooms
Nearest beach
Will consider Corporate bookings, House swap, Long term lets (over 1 month), Short breaks (1-4 days)
Access Car advised
Nearest Amenities 200 m
Nearest travel links Nearest airport: Geneva 100 km, Nearest railway: Les Houches 1 km
Family friendly Great for children of all ages, Suitable for people with restricted mobility
Notes Pets welcome, No smoking at this property
Features and Facilities

Luxuries Jacuzzi or hot tub, Sauna, Log fire, Internet access, DVD player
Pool Shared outdoor pool (unheated), Children's pool
General Central heating, TV, CD player, Table tennis, Safe, Satellite TV, Wi-Fi available
Standard Kettle, Toaster, Iron, Hair dryer
Utilities Clothes dryer, Dishwasher, Cooker, Microwave, Fridge, Freezer, Washing machine
Rooms 5 bedrooms, 5 bathrooms of which 5 En suites
Furniture Single beds (10), Cots (1), Dining seats for 12, Lounge seats for 12
Other High chair
Outdoors Shared outdoor pool (unheated), Balcony or terrace, Private garden, Shared garden, BBQ, Swing set
Access Parking
Further details indoors
With a myriad of chalets to choose from Chalet Fern Byre offers you something very special, the wonderful aimbience of a 230yr old Chamonix farmhouse married with modern, luxurious facilities. Owned and renovated by us over 5 years the Farm has been a labour of love..! but the attention to detail and quality of materials used has resulted in a very special property adored by all who stay.
Facilities include deep Italian leather sofa's juxtaposed with local mountain antiques and a modern granite and stainless steel kitchen married with hand-build cupboards. In the 5 bedrooms we have provided hotel standard zip-link beds so any room can be a double or a twin. We offer crisp, white, organic bed linen, goose feather duvets and leave you exclusive VOLA skincare bathroom products. The bathrooms are beautifully finished using Italian limestone tiles.
Wonderful valley views are framed from the huge picture windows, velux's and glass doors leading to the balcony. Our Eco features include geothermal generated underfloor heating, rain-water capture, clarivane double glazing, use of Dorvaplank, and re-use of the original wooden panels throughout providing a warm and indulgent ambience.
In the summer months we offer a private garden, ideal for al fresco dining plus the 'Swim-spa' hot tub provides a brilliant 'splash' pool for kids. We adorn the chalet with hanging baskets and can even offer a free minibus to Chamonix every morning for our B&B guests!
Chalet Fern Byre consists of the 2 upper floors of an ancient Alpine Farmhouse, with approximately 220 m2 of living space. The ground floor of the chalet is private (used by staff)
Further details outdoors
In Winter we provide bath-robes and crocs for the exterior 6m x 2.2m 'Swim Spa' hot tub, perfect for apres ski lounging!
In the summer months we offer a private side garden with BBQ, garden furniture, swings, table-tennis and the 'Swim-spa' hot tub provides a brilliant 'splash' pool for kids. We adorn the chalet with hanging baskets and the flower-covered balcony provides an ideal location for enjoying a cool drink and admiring the wonderful views.
Further details
Winter rentals are exclusive for groups. Rentals can be catered or self catered, for weeks or weekends, we are very flexible!
All Holidays can include our minibus service and airport transfers. Credit cards accepted.
Free concierge to book all ski packs, lessons or summer guides and mountain bikes.
Breakages deposit required for all rentals.
Summer holidays are self-catered or B&B.
Pressure washer available for mountian bikes.
The Rhone/French Alps region

The Mont Blanc massif offers an adrenalin packed holiday destination both winter and summer!

In winter you could ski 3 countries in one holiday! France, Switzerland and Italy! Boundless pistes and off piste variations including the famous 21km Combe Argentée trail (with a Guide)

In summer you can walk the 'Circuit des Crêtes Grises' and visit a host of charming villages and towns whilst admiring stunning Alpine pastures packed with the flora and fauna of the High Alps.

Locations worthy of a visit include Lake Annecy and the Old town of Annecy, the Pointe de Vorlan cable-car (Chamonix) for a wonderful view of the Alps and the Mont Blanc at 4807m (the highest mountain Peak in Europe). The Ice caves (accessed by the Belrioz railway) of the Combe Argentée are also worth a visit and for culture, Lyon, with its myriad of excellent shopping and restaurants and local exhibitions and museums.

Chamonix

Home to the sports of skiing and mountaineering, Chamonix is simply addictive. The dramatic mountains of the Chamonix valley incorporating the Mont Blanc Massif offers breathtaking scenery and make it a stunning setting for any skiing, snowboarding or summer activity holiday. With five separate ski areas scattered along the Chamonix valley, each with its own unique character and the famous off piste Combe Argentée run , every level of skier and snowboarder is amply catered for!

Les Houches is a pretty and unspoilt ski village which nestles just 5km from Chamonix town.

Les Houches is the largest single, pisted area in the Chamonix valley and has the added bonus of 86 snow canons covering 23 hectares of piste, this ski domain has wonderful skiing for beginners, intermediates and especially families.

The Chamonix valley has plenty to offer the non-skier, both rich in history and buzzing with shops, markets, bars, restaurants, exhibitions and festivals. There is also an seemingly unlimited variety of activities, from rock and ice climbing or snow shoe walking to x country and husky sledding. Chamonix is more than just a ski resort - it's a thriving mountain community, offering something for everyone. So join us this winter, you'll find our ski chalets simply gorgeous, our service attentive, our value for money excellent and your holiday experience simply unforgettable.

```html
<!DOCTYPE html>
<html lang="en">
<head>
<meta charset="utf-8">
<title>Fern Byre – Chamonix farmhouse chalet</title>
<link href="https://fonts.googleapis.com/css2?family=Arimo:wght@400;700&family=Open+Sans:wght@400;600&display=swap" rel="stylesheet">
<style>
  :root {
    --page-bg: #ffffff;
    --text-muted: #8a8a8a;
    --text-body: #7b7b7b;
    --text-strong: #222222;
    --text-soft: #c4c4c4;
    --rule: #dcdcdc;
    --accent: #d4e01a;
    --logo-ink: #1b1b1b;
    --nav-text: #8f8f8f;
  }
  * { box-sizing: border-box; margin: 0; padding: 0; }
  html, body {
    width: 1150px; height: 1200px; overflow: hidden;
    background: var(--page-bg);
    font-family: "Arimo", Arial, sans-serif;
  }
  .page { width: 960px; margin: 0 auto; padding-top: 30px; position: relative; }

  .site-tagline {
    text-align: center; font-size: 20px; color: var(--text-muted);
    padding-bottom: 7px; border-bottom: 1px dotted #c8c8c8;
  }

  .masthead { display: flex; justify-content: space-between; margin-top: 9px; height: 72px; }
  .brand { display: flex; align-items: center; gap: 14px; padding-left: 4px; }
  .brand-mark { width: 18px; height: 18px; background: var(--accent); }
  .brand-name {
    font-family: "Open Sans", Arial, sans-serif; font-size: 44px; font-weight: 400;
    color: var(--logo-ink); letter-spacing: -0.5px;
  }
  .intro-note {
    width: 315px; border-left: 1px solid var(--rule); padding: 2px 0 0 15px;
    font-size: 12px; line-height: 13.5px; color: var(--text-soft);
  }

  .nav-row { display: flex; justify-content: space-between; align-items: center; margin-top: 13px; }
  .main-nav { display: flex; list-style: none; gap: 0; }
  .main-nav li {
    font-size: 12px; color: var(--nav-text); padding: 5px 15px; margin-right: 0;
  }
  .main-nav li.is-current { background: var(--accent); color: #fff; }
  .search-field {
    width: 316px; height: 30px; border: 1px solid #e2e2e2; position: relative;
  }
  .search-field svg { position: absolute; right: 8px; top: 8px; }

  .hero-wrap { margin-top: 35px; position: relative; }
  .hero-photo {
    width: 959px; height: 578px; display: block; position: relative; z-index: 1;
    background: linear-gradient(180deg,
      #7fa9d8 0%, #a9c3df 14%, #5f7a57 26%, #3f6a2c 38%,
      #8a5a36 50%, #6d4a30 66%, #b4a08a 82%, #8fa3a8 100%);
  }
  .hero-shadow {
    height: 26px; margin: -4px 60px 0;
    background: radial-gradient(ellipse at top, rgba(0,0,0,0.28) 0%, rgba(0,0,0,0) 70%);
  }

  .welcome { margin-top: 8px; font-size: 12px; line-height: 14px; color: var(--text-body); }
  .welcome p + p { margin-top: 9px; }

  .site-footer {
    margin-top: 48px; border-top: 1px solid var(--rule); padding-top: 10px;
    display: flex;
  }
  .footer-col { width: 239px; border-left: 1px solid var(--rule); padding-left: 20px; height: 128px; }
  .footer-col:first-child { border-left: none; padding-left: 0; width: 219px; }
  .footer-col h3 { font-size: 12px; font-weight: 400; color: var(--text-strong); margin-top: 10px; margin-bottom: 9px; }
  .footer-col ul { list-style: none; }
  .footer-col li { font-size: 12px; color: #555; line-height: 18.7px; }
  .copyright { text-align: right; font-size: 11px; color: #666; margin-top: 13px; padding-right: 10px; }
</style>
</head>
<body>
<div class="page">
  <header>
    <h1 class="site-tagline" style="font-weight:400">Fern Byre - a 230yr old Chamonix farmhouse married with modern, luxurious facilities</h1>
    <div class="masthead">
      <div class="brand">
        <span class="brand-mark"></span>
        <span class="brand-name">Fern Byre</span>
      </div>
      <p class="intro-note">A rare find, Fern Byre dates from 1781 and offers the discerning skier a wonderful mountain lodge whilst also providing an impressive array of eco credentials to satisfy the environmentally conscious amongst us!</p>
    </div>
    <div class="nav-row">
      <ul class="main-nav">
        <li class="is-current">Home</li>
        <li>About</li>
        <li>Availability</li>
        <li>Gallery</li>
        <li>Price</li>
        <li>Location</li>
        <li>Book your stay</li>
      </ul>
      <div class="search-field">
        <svg width="14" height="14" viewBox="0 0 14 14" aria-hidden="true">
          <circle cx="5.5" cy="5.5" r="4" fill="none" stroke="#999" stroke-width="1.6"/>
          <line x1="8.5" y1="8.5" x2="12.5" y2="12.5" stroke="#999" stroke-width="2" stroke-linecap="round"/>
        </svg>
      </div>
    </div>
  </header>

  <main>
    <div class="hero-wrap">
      <div class="hero-photo" role="img" aria-label="Photograph of the old wooden farmhouse chalet with flower-decked balcony and hot tub, set against green forested mountains and a snowy peak under blue sky"></div>
      <div class="hero-shadow"></div>
    </div>
    <section class="welcome">
      <p>With a myriad of chalets to choose from Chalet Fern Byre offers you something very special, the wonderful aimbience of a 230yr old Chamonix farmhouse married with modern, luxurious facilities. Owned and renovated by us over 5 years the Farm has been a labour of love..! but the attention to detail and quality of materials used has resulted in a very special property adored by all who stay.</p>
      <p>Facilities include deep Italian leather sofa's juxtaposed with local mountain antiques, a modern granite and stainless steel kitchen married with hand-build cupboards. In the bedrooms, Superking or twin divan beds, organic bed linen, goose feather duvets and beautifully finished bathrooms using Italian limestone tiles. As operators for 25 winters your holiday will be expertly delivered by dedicated professionals who are here to ensure you will have a truly relaxing break.</p>
    </section>
  </main>

  <footer>
    <div class="site-footer">
      <div class="footer-col">
        <h3>SOCIAL</h3>
        <ul><li>Friendwall</li><li>Chirpline</li><li>Scrapfold</li><li>Shotboard</li><li>Sproutly</li></ul>
      </div>
      <div class="footer-col">
        <h3>HEADER</h3>
        <ul><li>More stuff</li><li>More stuff</li><li>More stuff</li><li>More stuff</li><li>More stuff</li></ul>
      </div>
      <div class="footer-col">
        <h3>HEADER</h3>
        <ul><li>More stuff</li><li>More stuff</li><li>More stuff</li><li>More stuff</li><li>More stuff</li></ul>
      </div>
      <div class="footer-col">
        <h3>CONTACT</h3>
        <ul><li>Fern Byre</li><li>Tel: 1-800-555-0140</li><li>Fax: 1-800-555-0141</li><li>contact@fernbyre.com</li></ul>
      </div>
    </div>
    <p class="copyright">Copyright 2014. All Rights Reserved.</p>
  </footer>
</div>
</body>
</html>
```